Business and Success Coaching Business Card

Need a business card for my coaching business. I coach small businesses, career professionals and, individuals wanting to unlock their human potential and achieve excellence. At the heart of our methodology is the Shaping Purposeful Action Routines Knowingly (SPARK) approach to formulate empowerment, create principles for success and setting achievable outcomes. I would like something that incorporates our new logo, something clean and sharp with a solid darker, but complementary background, color on the card front. The back should be white where there will be room for three questions

Target Market(s)

People looking to advance and improve themselves through a success coach

Industry/Entity Type

Life Coaching

Contact Information for Business Card

Contact information on card.
Business name on front of card
Questions on back

Font styles to use
Other font styles liked:
• Century Gothic or other Serif style fonts that look similar to Century Gothic

Colors

Designer to choose colors to be used in the design.

Requirements
Must have
• Logo on front of card
• Business name - The Steady Forge
• Contact name - Ted Harlow
• Address - Box 4619, Littleton, CO 80127-4619
• Phone number - 303-555-0147
• Email address - harlow.ted@thesteadyforge.example
• Certifications - CSC, CCHt, PTT, PNLP
• Back of card
• Three questions on the back of the card:
• If you were at your best, what would you do right now?
• What is the decision you have been avoiding?
• What's one action you could take in the next 10 minutes?
Nice to have
• I would like to see a solid color on the front of the card that compliments the logo.
• Back should be white, or could be contrasting, but need to have the three questions.

```html
<!DOCTYPE html>
<html lang="en">
<head>
<meta charset="utf-8">
<title>The Steady Forge – Business Card</title>
<link rel="stylesheet" href="https://fonts.googleapis.com/css2?family=Roboto:wght@400;500;700&display=swap">
<style>
  :root {
    --navy: #1f3570;
    --sky: #4a86c8;
    --ink: #333a45;
    --card: #ffffff;
    --backdrop: #efefef;
  }
  * { margin: 0; padding: 0; box-sizing: border-box; }
  html, body { width: 1200px; height: 1180px; overflow: hidden; }
  body {
    position: relative;
    background: var(--backdrop);
    font-family: "Roboto", Arial, sans-serif;
    color: var(--navy);
  }
  .card {
    position: absolute;
    left: 231px;
    width: 748px;
    height: 428px;
    background: var(--card);
    border-radius: 22px;
  }
  .card--questions { top: 108px; }
  .card--contact { top: 651px; }

  /* Brand lockup */
  .brand {
    position: absolute;
    display: flex;
    flex-direction: column;
    align-items: center;
  }
  .brand__dot {
    border-radius: 50%;
    background: var(--navy);
  }
  .brand__name {
    font-weight: 700;
    color: var(--navy);
    white-space: nowrap;
  }
  .card--questions .brand { left: 0; right: 0; top: 42px; }
  .card--questions .brand__dot { width: 96px; height: 96px; margin-bottom: 22px; }
  .card--questions .brand__name { font-size: 34px; }

  .card--contact .brand { left: 436px; width: 270px; top: 250px; }
  .card--contact .brand__dot { width: 76px; height: 76px; margin-bottom: 16px; }
  .card--contact .brand__name { font-size: 27px; }

  /* Questions */
  .questions { position: absolute; left: 37px; top: 254px; list-style: none; }
  .question {
    display: flex;
    align-items: center;
    height: 34px;
    margin-bottom: 21px;
  }
  .question__icon { width: 60px; height: 30px; margin-right: 21px; flex: none; }
  .question__text {
    width: 588px;
    height: 34px;
    line-height: 34px;
    padding-left: 13px;
    background: var(--navy);
    color: #fff;
    font-size: 20.5px;
    white-space: nowrap;
  }

  /* Contact side */
  .company-title {
    position: absolute;
    left: 43px;
    top: 56px;
    font-size: 37px;
    font-weight: 700;
  }
  .person { position: absolute; left: 43px; top: 230px; }
  .person__name { font-size: 37px; font-weight: 700; line-height: 1.1; }
  .person__creds { font-size: 16.5px; color: var(--ink); margin-top: 6px; }
  .person__rule { width: 28px; height: 3px; background: var(--navy); margin: 12px 0 14px; }
  .contact-list { list-style: none; }
  .contact-item {
    display: flex;
    align-items: center;
    height: 27px;
    font-size: 16.5px;
    color: var(--ink);
  }
  .contact-item svg { width: 16px; height: 16px; margin-right: 12px; flex: none; }
</style>
</head>
<body>

<section class="card card--questions">
  <div class="brand">
    <span class="brand__dot"></span>
    <span class="brand__name">The Steady Forge</span>
  </div>
  <ol class="questions">
    <li class="question">
      <svg class="question__icon" viewBox="0 0 60 30" aria-hidden="true"><path d="M2 10h36V2l20 13-20 13v-8H2z" fill="var(--navy)"/></svg>
      <span class="question__text">If you were at your best, what would you do right now?</span>
    </li>
    <li class="question">
      <svg class="question__icon" viewBox="0 0 60 30" aria-hidden="true"><path d="M2 10h36V2l20 13-20 13v-8H2z" fill="var(--navy)"/></svg>
      <span class="question__text">What is the decision you have been avoiding?</span>
    </li>
    <li class="question">
      <svg class="question__icon" viewBox="0 0 60 30" aria-hidden="true"><path d="M2 10h36V2l20 13-20 13v-8H2z" fill="var(--navy)"/></svg>
      <span class="question__text">What's one action you could take in the next 10 minutes?</span>
    </li>
  </ol>
</section>

<section class="card card--contact">
  <h1 class="company-title">The Steady Forge</h1>
  <div class="person">
    <h2 class="person__name">Ted Harlow</h2>
    <p class="person__creds">CSC, CCHt, PTT, PNLP</p>
    <div class="person__rule"></div>
    <ul class="contact-list">
      <li class="contact-item">
        <svg viewBox="0 0 16 16" aria-hidden="true"><rect width="16" height="16" rx="3" fill="var(--navy)"/><path d="M5 3.5l1.6 2.4-1 1c.6 1.3 1.5 2.2 2.8 2.8l1-1 2.4 1.6-.8 1.8c-3.8-.3-7-3.5-7.3-7.3z" fill="#fff"/></svg>
        303-555-0147
      </li>
      <li class="contact-item">
        <svg viewBox="0 0 16 16" aria-hidden="true"><rect width="16" height="16" rx="3" fill="var(--navy)"/><rect x="3.5" y="5" width="9" height="6.5" fill="none" stroke="#fff" stroke-width="1.2"/><path d="M3.5 5l4.5 3.5L12.5 5" fill="none" stroke="#fff" stroke-width="1.2"/></svg>
        harlow.ted@thesteadyforge.example
      </li>
      <li class="contact-item">
        <svg viewBox="0 0 16 16" aria-hidden="true"><rect width="16" height="16" rx="3" fill="var(--navy)"/><path d="M8 13s-3.5-3.6-3.5-6.2a3.5 3.5 0 017 0C11.5 9.4 8 13 8 13z" fill="#fff"/><circle cx="8" cy="6.8" r="1.3" fill="var(--navy)"/></svg>
        Box 4619, Littleton, CO 80127-4619
      </li>
    </ul>
  </div>
  <div class="brand">
    <span class="brand__dot"></span>
    <span class="brand__name">The Steady Forge</span>
  </div>
</section>

</body>
</html>
```